Labels designs for a new coffee brand (Velloru Coffee)

We looking for a coffee label design for our coffee Brand, VELLORU COFFE, attached is the logo. We are bringing out to the market 3 Premium blends
1. Colombian Popayan
2. Gourmet Expresso Blend
3. Brazilian Santos

We like something that looks high quality yet modern, the bags we are using is black matte, we are starting with labels and look in the near future to print our own labels .

We want the labels for the 3 coffees to have the similar look and feel but to be uniquely identified by its design (Colombian, Brazilian, espresso) This is beig sold as a set so we want it to have a similar label feeling but that each is identify as its unique product (colombian, expresso, brazilian blend.

This project is for labels that will be used on a black matte bag, is for a 16 oz bag,

Attached is a sample of the bag color.

Size Requirements:
Maintain a 2:3 aspect ratio for the image file
The label will be 4" wide and 6" tall (we also want to print some 3X4)
Recommended image size is 1600px X 2400px

I will provide upc later

www.vellorucoffee.example pw 12345 this is the test site not live yet but you can get a feel of the brand

Ay my daughters volleyball tournament I need extra time to review

coffee drinkers

coffee

• Creativity, unique, eye catchy,

```html
<!DOCTYPE html>
<html lang="en">
<head>
<meta charset="utf-8">
<title>Velloru Coffee – Premium Blend Labels</title>
<link rel="stylesheet" href="https://fonts.googleapis.com/css2?family=Josefin+Sans:wght@600;700&family=Montserrat:wght@600;700;800&family=Roboto:wght@300&display=swap">
<style>
  :root {
    --page: #ffffff;
    --label: #ece3d3;
    --brand-brown: #9a603a;
    --ink: #1c1410;
    --body-light: #9b6743;
    --body-dark: #5e3e27;
    --rule: #efe4d6;
    --white: #ffffff;
    --red-a: #d2461a;
    --red-b: #9b1410;
    --green-a: #0b9278;
    --green-b: #055c49;
    --crimson-a: #cc1040;
    --crimson-b: #8d1030;
  }
  * { box-sizing: border-box; margin: 0; padding: 0; }
  html, body { width: 1200px; height: 873px; overflow: hidden; background: var(--page); }
  .canvas { position: relative; width: 1200px; height: 873px; }

  .label {
    position: absolute; top: 179px; width: 348px; height: 521px;
    background: var(--label);
    box-shadow: 0 1px 2px rgba(0,0,0,.35);
  }
  .label--red { left: 67px; --accent-a: var(--red-a); --accent-b: var(--red-b); }
  .label--green { left: 426px; top: 176px; --accent-a: var(--green-a); --accent-b: var(--green-b); }
  .label--crimson { left: 785px; top: 178px; --accent-a: var(--crimson-a); --accent-b: var(--crimson-b); }

  .tagline { position: absolute; left: 0; top: 0; width: 348px; height: 60px; overflow: visible; }
  .tagline text { font-family: "Montserrat", sans-serif; fill: var(--ink); }
  .tagline .arc { font-size: 10.5px; font-weight: 700; letter-spacing: 2px; }
  .tagline .est { font-size: 7.5px; font-weight: 800; }

  .brand {
    position: absolute; top: 94px; left: 0; width: 348px;
    display: flex; align-items: center; justify-content: center; gap: 10px;
    font-family: "Josefin Sans", sans-serif; font-weight: 600;
    font-size: 36px; letter-spacing: 2px; color: var(--brand-brown); line-height: 1;
  }
  .brand__dot { width: 30px; height: 30px; border-radius: 50%; background: var(--brand-brown); margin-top: -6px; }

  .panel {
    position: absolute; left: 33px; top: 182px; width: 291px; height: 297px;
    border-radius: 13px; overflow: hidden;
    background: linear-gradient(90deg, var(--body-light), var(--body-dark));
    color: var(--white);
  }
  .panel__head {
    position: absolute; left: 0; top: 0; width: 100%; height: 97px;
    background: linear-gradient(90deg, var(--accent-a), var(--accent-b));
  }
  .blend-name {
    position: absolute; top: 35px; width: 100%; text-align: center;
    font-family: "Josefin Sans", sans-serif; font-weight: 700;
    font-size: 24px; line-height: 24px; letter-spacing: .2px;
  }
  .origin { position: absolute; left: 30px; top: 140px; font-family: "Josefin Sans", sans-serif; font-weight: 700; font-size: 12px; }
  .notes { position: absolute; left: 30px; top: 154px; font-family: "Roboto", sans-serif; font-weight: 300; font-size: 8px; }
  .rule { position: absolute; background: var(--rule); }
  .rule--top { left: 30px; top: 169px; width: 235px; height: 1px; }
  .rule--mid { left: 104px; top: 213px; width: 161px; height: 1px; }
  .rule--grind { left: 40px; top: 217px; width: 52px; height: 1px; }
  .rule--vert { left: 104px; top: 169px; width: 1px; height: 90px; }
  .grind {
    position: absolute; left: 34px; width: 60px; text-align: center;
    font-family: "Montserrat", sans-serif; font-weight: 800; font-size: 7.8px; line-height: 9px;
  }
  .grind--ground { top: 192px; }
  .grind--bean { top: 232px; }
  .spec { position: absolute; top: 182px; }
  .spec strong { display: block; font-family: "Josefin Sans", sans-serif; font-weight: 700; font-size: 11px; line-height: 11px; }
  .spec span { display: block; font-family: "Roboto", sans-serif; font-weight: 300; font-size: 8px; line-height: 10px; }
  .spec--purity { left: 116px; }
  .spec--weight { left: 206px; }
  .site {
    position: absolute; left: 104px; width: 161px; top: 234px; text-align: center;
    font-family: "Montserrat", sans-serif; font-weight: 700; font-size: 6.5px; letter-spacing: 1.3px;
  }

  .seal { position: absolute; left: 259px; top: 428px; width: 76px; height: 76px; }
  .seal .edge { fill: url(#sealFill); stroke: #c9c9c9; }
</style>
</head>
<body>
<svg width="0" height="0" style="position:absolute">
  <defs>
    <path id="arcPath" d="M60 56 Q184 8 308 56"/>
    <radialGradient id="sealFill" cx="35%" cy="30%" r="80%">
      <stop offset="0" stop-color="#ffffff"/>
      <stop offset="1" stop-color="#cdcdcd"/>
    </radialGradient>
  </defs>
</svg>

<main class="canvas">

  <article class="label label--red">
    <svg class="tagline" viewBox="0 0 348 60">
      <text class="arc"><textPath href="#arcPath" startOffset="50%" text-anchor="middle">- SMALL-BATCH ROASTED -</textPath></text>
      <text class="est" x="180" y="48" text-anchor="middle">• EST. 2023 •</text>
    </svg>
    <div class="brand"><span class="brand__dot"></span>VELLORU</div>
    <section class="panel">
      <div class="panel__head"></div>
      <h2 class="blend-name">COLOMBIAN<br>POPAYAN</h2>
      <p class="origin">COLOMBIAN</p>
      <p class="notes">Notes of panela, red apple, milk chocolate</p>
      <i class="rule rule--top"></i><i class="rule rule--vert"></i><i class="rule rule--mid"></i><i class="rule rule--grind"></i>
      <p class="grind grind--ground">REGULAR<br>GROUND</p>
      <p class="grind grind--bean">WHOLE<br>BEAM</p>
      <p class="spec spec--purity"><strong>100%</strong><span>Cafe Arabica</span></p>
      <p class="spec spec--weight"><strong>16 Oz</strong><span>454 gr</span></p>
      <p class="site">VELLORUCOFFEE.EXAMPLE</p>
    </section>
    <svg class="seal" viewBox="0 0 76 76">
      <circle class="edge" cx="38" cy="38" r="34" stroke-width="1"/>
      <circle cx="38" cy="38" r="35" fill="none" stroke="#e4e4e4" stroke-width="5" stroke-linecap="round" stroke-dasharray="0 7.3"/>
      <circle cx="38" cy="38" r="11" fill="var(--accent-a)"/>
    </svg>
  </article>

  <article class="label label--green">
    <svg class="tagline" viewBox="0 0 348 60">
      <text class="arc"><textPath href="#arcPath" startOffset="50%" text-anchor="middle">- SMALL-BATCH ROASTED -</textPath></text>
      <text class="est" x="180" y="48" text-anchor="middle">• EST. 2023 •</text>
    </svg>
    <div class="brand"><span class="brand__dot"></span>VELLORU</div>
    <section class="panel">
      <div class="panel__head"></div>
      <h2 class="blend-name">GOURMET EXPRESSO<br>BLEND</h2>
      <p class="origin">COLOMBIAN</p>
      <p class="notes">Notes of dark brown sugar, gianduja, cream</p>
      <i class="rule rule--top"></i><i class="rule rule--vert"></i><i class="rule rule--mid"></i><i class="rule rule--grind"></i>
      <p class="grind grind--ground">REGULAR<br>GROUND</p>
      <p class="grind grind--bean">WHOLE<br>BEAM</p>
      <p class="spec spec--purity"><strong>100%</strong><span>Cafe Arabica</span></p>
      <p class="spec spec--weight"><strong>16 Oz</strong><span>454 gr</span></p>
      <p class="site">VELLORUCOFFEE.EXAMPLE</p>
    </section>
    <svg class="seal" viewBox="0 0 76 76">
      <circle class="edge" cx="38" cy="38" r="34" stroke-width="1"/>
      <circle cx="38" cy="38" r="35" fill="none" stroke="#e4e4e4" stroke-width="5" stroke-linecap="round" stroke-dasharray="0 7.3"/>
      <circle cx="38" cy="38" r="11" fill="var(--accent-a)"/>
    </svg>
  </article>

  <article class="label label--crimson">
    <svg class="tagline" viewBox="0 0 348 60">
      <text class="arc"><textPath href="#arcPath" startOffset="50%" text-anchor="middle">- SMALL-BATCH ROASTED -</textPath></text>
      <text class="est" x="180" y="48" text-anchor="middle">• EST. 2023 •</text>
    </svg>
    <div class="brand"><span class="brand__dot"></span>VELLORU</div>
    <section class="panel">
      <div class="panel__head"></div>
      <h2 class="blend-name">BRAZILIAN<br>SANTOS</h2>
      <p class="origin">BRAZILIAN</p>
      <p class="notes">Notes of roasted nuts, cocoa, soft caramel</p>
      <i class="rule rule--top"></i><i class="rule rule--vert"></i><i class="rule rule--mid"></i><i class="rule rule--grind"></i>
      <p class="grind grind--ground">REGULAR<br>GROUND</p>
      <p class="grind grind--bean">WHOLE<br>BEAM</p>
      <p class="spec spec--purity"><strong>100%</strong><span>Cafe Arabica</span></p>
      <p class="spec spec--weight"><strong>16 Oz</strong><span>454 gr</span></p>
      <p class="site">VELLORUCOFFEE.EXAMPLE</p>
    </section>
    <svg class="seal" viewBox="0 0 76 76">
      <circle class="edge" cx="38" cy="38" r="34" stroke-width="1"/>
      <circle cx="38" cy="38" r="35" fill="none" stroke="#e4e4e4" stroke-width="5" stroke-linecap="round" stroke-dasharray="0 7.3"/>
      <circle cx="38" cy="38" r="11" fill="var(--accent-a)"/>
    </svg>
  </article>

</main>
</body>
</html>
```